quality electrical business needs a logo design

we need a logo design for our new company starting up. I'm a sole trader electrician. I want to make the PES prominent in Perant Electrical Services. Information I would want on the business card would be;
Business Name: Perant Electrical Services
What I do: Domestic/Commercial/Industrial Installation & Maintenance
Email Address: Bryce.perant@wavlo.net.au
Contact no: Bryce 0438261759
Electrical License no: EC57364

Open to different Colours but would like to see some with Navy blue. I want to promote professionalism and have a modern feel about it.

Industry/Entity Type

Electrical

```html
<!DOCTYPE html>
<html lang="en">
<head>
<meta charset="utf-8">
<title>Perant Electrical Services – Business Card</title>
<link rel="stylesheet" href="https://fonts.googleapis.com/css2?family=Arimo:wght@400;700&display=swap">
<style>
  :root {
    --backdrop: #2b2f31;
    --card-white: #ffffff;
    --navy: #1f2466;
    --navy-deep: #0d103f;
    --navy-mid: #262d78;
    --text-light: #ffffff;
  }
  * { box-sizing: border-box; margin: 0; padding: 0; }
  html, body {
    width: 1200px;
    height: 750px;
    overflow: hidden;
    background: var(--backdrop);
    font-family: "Arimo", Arial, sans-serif;
  }
  .card {
    position: absolute;
    left: 80px;
    top: 60px;
    width: 1040px;
    height: 630px;
    background: var(--card-white);
    overflow: hidden;
    box-shadow: 0 12px 40px rgba(0,0,0,.45);
  }
  .brand {
    position: absolute;
    left: 300px;
    top: 70px;
    width: 560px;
    text-align: center;
    color: var(--navy);
  }
  .brand-name {
    display: inline-flex;
    align-items: center;
    gap: 14px;
    font-size: 62px;
    font-weight: 700;
    letter-spacing: 1px;
    line-height: 1;
  }
  .brand-mark {
    width: 22px;
    height: 22px;
    background: var(--navy);
  }
  .brand-tagline {
    margin-top: 6px;
    font-size: 52px;
    font-weight: 400;
    line-height: 1.1;
  }
  .services {
    position: absolute;
    left: 0;
    top: 292px;
    width: 100%;
    height: 36px;
    color: var(--navy);
    font-size: 25px;
  }
  .service {
    position: absolute;
    bottom: 0;
    display: flex;
    align-items: flex-end;
    gap: 4px;
  }
  .service svg { width: 14px; height: 28px; }
  .service--commercial { left: 28px; }
  .service--industrial { left: 330px; }
  .service--domestic { left: 830px; }
  .rule {
    position: absolute;
    left: 0;
    width: 100%;
    background: var(--navy);
  }
  .rule--upper { top: 332px; height: 3px; }
  .rule--lower { top: 340px; height: 2px; }
  .contact-band {
    position: absolute;
    left: 0;
    top: 348px;
    width: 100%;
    height: 282px;
    background: linear-gradient(180deg, var(--navy-mid) 0%, var(--navy) 35%, var(--navy-deep) 100%);
    color: var(--text-light);
  }
  .contact-name {
    position: absolute;
    left: 58px;
    top: 10px;
    font-size: 38px;
    font-weight: 400;
  }
  .contact-row {
    position: absolute;
    left: 62px;
    display: flex;
    align-items: center;
    gap: 40px;
    font-size: 22px;
  }
  .contact-row--phone { top: 58px; }
  .contact-row--email { top: 138px; }
  .contact-row svg { flex: none; }
  .licence {
    position: absolute;
    left: 62px;
    top: 222px;
    font-size: 22px;
  }
  .licence-label { font-weight: 700; margin-right: 8px; }
</style>
</head>
<body>
  <main class="card">
    <header class="brand">
      <div class="brand-name"><span class="brand-mark"></span>Perant</div>
      <div class="brand-tagline">Electrical Services</div>
    </header>

    <ul class="services">
      <li class="service service--commercial">
        <svg viewBox="0 0 14 28"><polygon points="9,0 2,15 7,15 4,28 12,11 7,11 11,0" fill="currentColor"/></svg>Commercial
      </li>
      <li class="service service--industrial">
        <svg viewBox="0 0 14 28"><polygon points="9,0 2,15 7,15 4,28 12,11 7,11 11,0" fill="currentColor"/></svg>Industrial Installation &amp; Maintenance
      </li>
      <li class="service service--domestic">
        <svg viewBox="0 0 14 28"><polygon points="9,0 2,15 7,15 4,28 12,11 7,11 11,0" fill="currentColor"/></svg>Domestic
      </li>
    </ul>

    <div class="rule rule--upper"></div>
    <div class="rule rule--lower"></div>

    <section class="contact-band">
      <h2 class="contact-name">Bryce</h2>
      <div class="contact-row contact-row--phone">
        <svg width="30" height="54" viewBox="0 0 30 54" aria-hidden="true">
          <rect x="3" y="2" width="24" height="50" rx="4" fill="none" stroke="#fff" stroke-width="3"/>
          <rect x="8" y="8" width="14" height="14" fill="#fff"/>
          <g fill="#fff">
            <rect x="8" y="27" width="4" height="4"/><rect x="13" y="27" width="4" height="4"/><rect x="18" y="27" width="4" height="4"/>
            <rect x="8" y="33" width="4" height="4"/><rect x="13" y="33" width="4" height="4"/><rect x="18" y="33" width="4" height="4"/>
            <rect x="8" y="39" width="4" height="4"/><rect x="13" y="39" width="4" height="4"/><rect x="18" y="39" width="4" height="4"/>
          </g>
        </svg>
        <span>0438261759</span>
      </div>
      <div class="contact-row contact-row--email">
        <svg width="46" height="34" viewBox="0 0 46 34" aria-hidden="true">
          <rect x="2" y="2" width="42" height="30" fill="none" stroke="#fff" stroke-width="3"/>
          <polyline points="2,2 23,20 44,2" fill="none" stroke="#fff" stroke-width="3"/>
          <line x1="2" y1="32" x2="18" y2="16" stroke="#fff" stroke-width="3"/>
          <line x1="44" y1="32" x2="28" y2="16" stroke="#fff" stroke-width="3"/>
        </svg>
        <span>Bryce.perant@wavlo.net.au</span>
      </div>
      <p class="licence"><span class="licence-label">License:</span>EC57364</p>
    </section>
  </main>
</body>
</html>
```